Company Profile
Korvane Cargo Sdn Bhd is a well-established and experienced freight forwarder in Kuala Lumpur, Malaysia. We specialize in air and sea forwarding, Custom Brokerage and regulatory compliance services, inland transportation, overseas freighting and warehousing and distribution management. With our dedicated qualified and experienced professionals, we are fully committed to serving our clients.

Our Mission
Based on the motto “Quick, Reliable and Polite”, Korvane Cargo is dedicated to upholding the following three points corporate philosophy:1. Adhering to the principle that “the customer always comes first”.2. Contributing to the development of the local community.3. Making it our duty to be responsible and sincere.

Our Edge
• One-Stop Logistics Solutions
• Extensive Network Throughout Malaysia
• Highly Qualified and Experienced Pool of Professionals
• Comprehensive IT Solutions
• Innovative and Customer-focused Solutions
• Flexible and Consistent in Managing Exceptions
• Total Supply Chain Visibility

Target Market : We sell the logistics services to all the industry in Malaysia. (One Stop Logistics Solutions)

Business Card Detail : I would like to see the logo on the front with the general info.

Must Haves :
1) Name, Title, Office, Cell, Fax, Email, Address, Website
2) Must have complete company name show as : Korvane Cargo Sdn Bhd
3) Must have company registration no, show as : 8571620-W

Nice to Haves : Modern Design Business Card

Target Market(s)

We sell the logistics services to all the industry in Malaysia. (One Stop Logistics Solutions)

Contact Information for Business Card

I would like to see the logo on the front with the general info.

Colors

Designer to choose colors to be used in the design.

Requirements
Must have
• 1) Name, Title, Office, Cell, Fax, Email, Address, Website
• 2) Must have complete company name show as : Korvane Cargo Sdn Bhd
• 3) Must have company registration no, show as : 8571620-W
Nice to have
• Modern Design Business Card
Should not have
• Nil

```html
<!DOCTYPE html>
<html lang="en">
<head>
<meta charset="utf-8">
<title>Korvane Cargo – Business Card</title>
<link rel="stylesheet" href="https://fonts.googleapis.com/css2?family=Michroma&family=Roboto:wght@400;500;700&display=swap">
<style>
  :root{
    --bg:#2a2a2c;
    --navy:#0d4a8c;
    --blue:#1a72c4;
    --sky:#27aee6;
    --ink:#1a1a1a;
    --white:#ffffff;
    --faint:#eceff5;
  }
  *{box-sizing:border-box;margin:0;padding:0}
  html,body{width:1200px;height:895px;overflow:hidden;background:var(--bg);font-family:"Roboto",Arial,sans-serif}
  .card{position:absolute;width:620px;height:354px;border-radius:26px;overflow:hidden}

  /* back side */
  .card--back{left:60px;top:60px;background:radial-gradient(ellipse at 55% 45%,#2aa9e4 0%,#1b7cca 45%,#0f55a0 100%);color:var(--white)}
  .brand{position:absolute;display:flex;align-items:center;gap:14px}
  .brand__dot{width:44px;height:44px;border-radius:50%;border:4px solid currentColor;flex:none}
  .brand__name{font-family:"Roboto",Arial,sans-serif;font-weight:700;font-size:36px;letter-spacing:3px;text-transform:uppercase;line-height:1}
  .card--back .brand{left:150px;top:92px;color:var(--white)}
  .edge-list{position:absolute;top:200px;list-style:none;font-size:15px;line-height:20px}
  .edge-list li{padding-left:14px;position:relative}
  .edge-list li::before{content:"";position:absolute;left:0;top:7px;width:6px;height:6px;border-radius:50%;background:var(--white)}
  .edge-list--left{left:50px;top:228px;width:270px}
  .edge-list--right{left:330px;width:270px}

  /* front side */
  .card--front{left:520px;top:480px;background:var(--white);color:var(--ink)}
  .card--front .brand{left:250px;top:38px;color:var(--navy)}
  .card--front .brand__name{font-size:30px}
  .ghost-ring{position:absolute;right:-70px;top:70px;width:260px;height:260px;border-radius:50%;border:18px solid var(--faint)}
  .person{position:absolute;left:0;top:120px;padding-left:34px;border-left:10px solid var(--sky)}
  .person__name{font-family:"Michroma",sans-serif;font-size:24px;color:var(--navy);line-height:1.1}
  .person__title{font-size:15px;color:var(--ink)}
  .office{position:absolute;left:44px;top:186px;font-size:14px;line-height:18px}
  .office__company{color:var(--sky);font-weight:700}
  .contacts{position:absolute;left:44px;top:258px;list-style:none;font-size:13.5px;line-height:16px}
  .contacts li{display:flex;align-items:center;gap:8px}
  .contacts svg{width:12px;height:12px;fill:var(--navy);flex:none}
  .stripe{position:absolute;left:0;bottom:0;width:100%;height:10px;background:var(--sky)}
  .reg-tab{position:absolute;right:0;bottom:10px;width:220px;height:34px;background:var(--navy);color:var(--white);font-weight:700;font-size:15px;display:flex;align-items:center;justify-content:center;border-top-left-radius:4px}
</style>
</head>
<body>

<section class="card card--back" aria-label="Business card back">
  <div class="brand"><span class="brand__dot"></span><span class="brand__name">Korvane Cargo</span></div>
  <ul class="edge-list edge-list--left">
    <li>One-Stop Logistics Solutions</li>
    <li>Extensive Network Throughout Malaysia</li>
    <li>Highly Qualified and Experienced Pool of Professionals</li>
  </ul>
  <ul class="edge-list edge-list--right">
    <li>Comprehensive IT Solutions</li>
    <li>Innovative and Customer-focused Solutions</li>
    <li>Flexible and Consistent in Managing Exceptions</li>
    <li>Total Supply Chain Visibility</li>
  </ul>
</section>

<section class="card card--front" aria-label="Business card front">
  <div class="ghost-ring"></div>
  <div class="brand"><span class="brand__dot"></span><span class="brand__name">Korvane Cargo</span></div>

  <div class="person">
    <p class="person__name">DARREN TAN</p>
    <p class="person__title">Managing Director</p>
  </div>

  <div class="office">
    <p class="office__company">KORVANE CARGO SDN BHD</p>
    <p>No.8B, 2nd Floor, Jalan Seri Tanjung 4/KS2,</p>
    <p>Taman Seri Andalas, 41300 Klang,</p>
    <p>Selangor Darul Ehsan, Malaysia.</p>
  </div>

  <ul class="contacts">
    <li><svg viewBox="0 0 12 12"><path d="M3 0h6a1 1 0 0 1 1 1v10a1 1 0 0 1-1 1H3a1 1 0 0 1-1-1V1a1 1 0 0 1 1-1zm0 2v7h6V2z"/></svg>(+6012) 480 2716</li>
    <li><svg viewBox="0 0 12 12"><path d="M2 1l2-1 2 3-1.5 1a6 6 0 0 0 3.5 3.5L9 6l3 2-1 2c-5 0-9-4-9-9z"/></svg>(+603) 3342 5810 / 5811</li>
    <li><svg viewBox="0 0 12 12"><path d="M3 0h6v4H3zM1 4h10v6H9v2H3v-2H1zm3 4v3h4V8z"/></svg>(+603) 3342 5812</li>
    <li><svg viewBox="0 0 12 12"><path d="M0 2h12v1L6 7 0 3zm0 2.5l6 4 6-4V10H0z"/></svg>darren.tan@korvanecargo.com.my</li>
    <li><svg viewBox="0 0 12 12"><path d="M6 0a6 6 0 1 0 0 12A6 6 0 0 0 6 0zm0 1.2c.8.8 1.3 2.3 1.4 4.2H4.6c.1-1.9.6-3.4 1.4-4.2zM1.2 6.6h2.2c.1 1.6.5 3 1.1 3.9a4.8 4.8 0 0 1-3.3-3.9zm3.4 0h2.8c-.1 1.8-.6 3.3-1.4 4.2-.8-.9-1.3-2.4-1.4-4.2zm4 0h2.2a4.8 4.8 0 0 1-3.3 3.9c.6-.9 1-2.3 1.1-3.9zm0-1.2c-.1-1.6-.5-3-1.1-3.9a4.8 4.8 0 0 1 3.3 3.9zm-5.2 0H1.2a4.8 4.8 0 0 1 3.3-3.9c-.6.9-1 2.3-1.1 3.9z"/></svg>www.korvanecargo.com.my</li>
  </ul>

  <div class="reg-tab">Reg.#8571620-W</div>
  <div class="stripe"></div>
</section>

</body>
</html>
```